1 Cup Pod - Regular and Decaf

I am looking for 2 package designs. When you open the uploaded file it show one for regular and one for decaf. The size is also on the example template. Both products with still be named Café Ordala, only things we are looking for is new colors and design of package. you can use up to 4 colors at this time.

We are open to all types of ideas and colors. the only thins is the regular and decaf must be different colors.

Requirements
Must have
• Must use the exact information used on front and back of both package design from the example template. The only thing is to add, 75702 next to where it says Tyler, TX

```html
<!DOCTYPE html>
<html lang="en">
<head>
<meta charset="utf-8">
<title>Café Ordala Decaffeinated – Single-Cup Pod Pouch</title>
<link rel="stylesheet" href="https://fonts.googleapis.com/css2?family=Cinzel:wght@600&family=Arimo:wght@400;700&display=swap">
<style>
  :root {
    --stage: #efefef;
    --pouch-green: #426c1f;
    --pouch-green-light: #54802c;
    --pouch-green-deep: #2c5012;
    --leaf-shade: rgba(30, 62, 10, 0.55);
    --band-green: #0f3c0a;
    --gold: #d9b45a;
    --ink-light: #ffffff;
  }
  * { box-sizing: border-box; margin: 0; padding: 0; }
  html, body { width: 1200px; height: 1000px; overflow: hidden; }
  body {
    background: var(--stage);
    font-family: "Arimo", Arial, sans-serif;
    position: relative;
  }
  .pouch {
    position: absolute;
    top: 236px;
    width: 503px;
    height: 502px;
    overflow: hidden;
    background: var(--pouch-green);
  }
  .pouch--front { left: 82px; }
  .pouch--back { left: 615px; }

  .pouch__artwork {
    position: absolute;
    inset: 0;
    background:
      radial-gradient(ellipse 140px 260px at 12% 55%, var(--leaf-shade), transparent 75%),
      radial-gradient(ellipse 150px 240px at 90% 62%, var(--leaf-shade), transparent 75%),
      radial-gradient(ellipse 220px 90px at 40% 8%, rgba(30, 62, 10, 0.35), transparent 75%),
      linear-gradient(180deg, var(--pouch-green-light) 0%, var(--pouch-green) 50%, var(--pouch-green-deep) 100%);
  }
  .pouch__seal {
    position: absolute;
    left: 0; right: 0; top: 0;
    height: 54px;
    background: rgba(255, 255, 255, 0.05);
    border-bottom: 1px solid rgba(255, 255, 255, 0.06);
  }
  .pouch__edge {
    position: absolute;
    inset: 0;
    box-shadow: inset 14px 0 18px -10px rgba(0, 0, 0, 0.35),
                inset -14px 0 18px -10px rgba(0, 0, 0, 0.35),
                inset 0 -16px 20px -12px rgba(0, 0, 0, 0.35);
  }
  .pouch__band {
    position: absolute;
    left: 0; right: 0;
    top: 200px;
    height: 130px;
    background: var(--band-green);
    opacity: 0.82;
  }

  .brand {
    position: absolute;
    left: 0; right: 0;
    text-align: center;
    font-family: "Cinzel", "Times New Roman", serif;
    font-weight: 600;
    color: var(--gold);
  }
  .brand__line { display: block; }
  .pouch--front .brand { top: 176px; font-size: 72px; line-height: 64px; }
  .pouch--back .brand { top: 118px; font-size: 34px; line-height: 32px; }

  .variant {
    position: absolute;
    left: 0; right: 0;
    text-align: center;
    font-family: "Cinzel", "Times New Roman", serif;
    font-weight: 600;
    color: var(--ink-light);
  }
  .pouch--front .variant { top: 334px; font-size: 22px; }
  .pouch--back .variant { top: 189px; font-size: 11px; }

  .product-info {
    position: absolute;
    left: 0; right: 0;
    top: 408px;
    text-align: center;
    color: var(--ink-light);
    font-size: 13.5px;
    line-height: 19px;
  }

  .directions {
    position: absolute;
    left: 0; right: 0;
    top: 238px;
    text-align: center;
    color: var(--ink-light);
    font-size: 10.5px;
    line-height: 13.5px;
  }
  .directions__title { font-weight: 700; }

  .maker {
    position: absolute;
    left: 0; right: 0;
    top: 376px;
    text-align: center;
    color: var(--ink-light);
    font-weight: 700;
  }
  .maker__name { font-size: 15px; line-height: 19px; }
  .maker__place { font-size: 11px; line-height: 16px; }
</style>
</head>
<body>

  <section class="pouch pouch--front" aria-label="Pouch front">
    <div class="pouch__artwork" role="img" aria-label="Green pouch background with faint engraved coffee branches, leaves and cherries"></div>
    <div class="pouch__seal"></div>
    <div class="pouch__band"></div>
    <div class="pouch__edge"></div>
    <h1 class="brand">
      <span class="brand__line">CAFÈ</span>
      <span class="brand__line">ORDALA</span>
    </h1>
    <p class="variant">DECAFFEINATED</p>
    <p class="product-info">Single-Cup Coffee Pod<br>Colombian 7g</p>
  </section>

  <section class="pouch pouch--back" aria-label="Pouch back">
    <div class="pouch__artwork" role="img" aria-label="Green pouch background with faint engraved coffee branches, leaves and cherries"></div>
    <div class="pouch__seal"></div>
    <div class="pouch__band"></div>
    <div class="pouch__edge"></div>
    <p class="brand">
      <span class="brand__line">CAFÈ</span>
      <span class="brand__line">ORDALA</span>
    </p>
    <p class="variant">DECAFFEINATED</p>
    <div class="directions">
      <p class="directions__title">DIRECTIONS:</p>
      <p>Carefully open package.</p>
      <p>DO NOT OPEN FILTER PACK</p>
      <p>Place single-cup coffee pod in brew basket or funnel.</p>
      <p>Follow the directions on your coffee maker.</p>
    </div>
    <div class="maker">
      <p class="maker__name">DELVANE &amp; SONS</p>
      <p class="maker__place">BROOKVALE, TEXAS 75810</p>
    </div>
  </section>

</body>
</html>
```